Website improvements and Adding Functionalities at https://quorin.net/tamberly

1.Search functionality
2.Payment process functionality
3. Application configuration
4. Registration functionality activation
5. Chat functionality
6.Language switching functionality (Portuguese & French)
7.Bespoke interactive modules
8. Automated web scraping and data synchronisation mechanisms
9. News Page
10.Webinar facilities
11. Basic SEO optimisation
12. Speed and performance optimisation
13. Security configuration
14. Google Analytics integration
15. Cross-browser and mobile testing
16. Website deployment and launch support

Target Market(s)

My target markets are companies, investors, suppliers and professionals with an interest in the Mozambican oil and gas sector

Industry/Entity Type

Oil and Gas

Coding

Coded - Design and coding required

Number of Pages Required

1 page

Requirements
Must have
• Improve the existing page at https://quorin.net/tamberly and add the following features to it: 1. Search functionality 2. Payment process functionality 3. Application configuration 4. Activation of registration functionality 5. Chat functionality 6. Language switching functionality (Portuguese & French) 7. Bespoke interactive modules 8. Automated web scraping and data synchronisation mechanisms 9. News Page

```html
<!DOCTYPE html>
<html lang="en">
<head>
<meta charset="utf-8">
<title>Tamberly Co — Mozambique Oil &amp; Gas Intelligence</title>
<link href="https://fonts.googleapis.com/css2?family=Bebas+Neue&family=Outfit:wght@300;400;500;600;700&display=swap" rel="stylesheet">
<style>
:root{
  --navy:#29244f;
  --navy-deep:#1f1b40;
  --orange:#ee4a1c;
  --orange-soft:#f6a27f;
  --cream:#f4f1ec;
  --ink:#1f1d33;
  --muted:#55535f;
  --line:#e6e1da;
  --white:#ffffff;
}
*{box-sizing:border-box;margin:0;padding:0}
html,body{width:1200px;height:4471px;overflow:hidden}
body{font-family:"Outfit",sans-serif;color:var(--ink);background:var(--white);font-size:11px;line-height:1.5}
.wrap{width:900px;margin:0 auto;position:relative}
h1,h2,.display{font-family:"Bebas Neue",sans-serif;font-weight:400;letter-spacing:.5px;color:var(--navy)}
.accent-bar{display:block;width:40px;height:3px;background:var(--orange);margin:8px auto 0}
.btn{display:inline-flex;align-items:center;justify-content:center;font-weight:500;font-size:11px;height:28px;padding:0 22px;border-radius:3px;border:1px solid transparent}
.btn-orange{background:var(--orange);color:#fff}
.btn-outline{border-color:#fff;color:#fff}

/* header */
.topbar{height:70px;display:flex;align-items:center}
.topbar .wrap{display:flex;align-items:center}
.brand{display:flex;align-items:center;gap:10px;width:285px}
.brand-dot{width:30px;height:30px;border-radius:50%;background:var(--navy)}
.brand-name{font-weight:700;font-size:16px;letter-spacing:2px;color:var(--navy);line-height:1}
.search-top{margin-left:0;width:323px;height:30px;border:1px solid var(--line);border-radius:3px;display:flex;align-items:center;justify-content:space-between;padding:0 10px;font-size:8.5px;color:#8a8790}
.top-actions{margin-left:auto;display:flex;align-items:center;gap:10px}
.lang{font-size:10px;display:flex;align-items:center;gap:4px}
.lang i{width:13px;height:13px;border-radius:50%;background:#3b4a9a;display:inline-block}
.btn-login{height:28px;border:1px solid var(--navy);border-radius:3px;padding:0 14px;display:flex;align-items:center;gap:6px;font-size:10.5px}
.btn-register{height:28px;padding:0 20px;background:var(--orange);color:#fff;border-radius:3px;display:flex;align-items:center;font-size:10.5px}
.mainnav{height:45px;border-top:1px solid var(--line)}
.mainnav ul{list-style:none;display:flex;justify-content:center;gap:42px;height:45px;align-items:center;font-size:10.5px;font-weight:600;color:var(--ink)}
.mainnav li.active{color:var(--orange);position:relative;height:45px;display:flex;align-items:center}
.mainnav li.active::before{content:"";position:absolute;top:-1px;left:-12px;right:-12px;height:2px;background:var(--orange)}

/* hero */
.hero{height:630px;position:relative;background:linear-gradient(90deg,#3a2a2a 0%,#5b3a2c 35%,#3f3542 60%,#4a2a26 100%);color:#fff;overflow:hidden}
.hero-photo{position:absolute;inset:0;background:radial-gradient(ellipse at 50% 40%,rgba(240,140,70,.35),transparent 60%),linear-gradient(180deg,rgba(31,27,64,.25),rgba(31,27,64,.55))}
.hero-inner{position:relative;text-align:center;padding-top:170px}
.hero h1{color:#fff;font-size:38px;line-height:1.02}
.hero p{font-size:10.5px;width:650px;margin:10px auto 0;line-height:1.5;color:#eee}
.search-panel{width:705px;margin:20px auto 0;background:rgba(41,36,79,.92);border-radius:6px;padding:12px 24px 0;text-align:left}
.sp-row{display:flex;gap:10px;align-items:flex-end}
.sp-field{font-size:9.5px}
.sp-field span{display:block;margin-bottom:5px}
.sp-input{height:28px;border:1px solid rgba(255,255,255,.25);background:rgba(255,255,255,.08);border-radius:3px;font-size:8.5px;color:#bbb;display:flex;align-items:center;justify-content:space-between;padding:0 10px}
.sp-search{height:28px;width:140px;background:var(--orange);border-radius:3px;display:flex;align-items:center;justify-content:center;gap:5px;font-size:10px}
.sp-tabs{display:flex;justify-content:center;gap:48px;height:40px;align-items:center;font-size:9.5px;margin-top:10px;border-top:1px solid rgba(255,255,255,.1)}
.sp-tabs span{display:flex;align-items:center;gap:6px}
.sp-tabs i{width:10px;height:10px;border:1.5px solid var(--orange);border-radius:2px;display:inline-block}
.hero-cta{margin-top:22px;display:flex;justify-content:center;gap:8px}
.chat-bubble{position:absolute;left:967px;top:540px;background:#fff;color:var(--ink);font-size:9.5px;line-height:1.3;padding:10px 14px;border-radius:6px;width:133px}
.chat-btn{position:absolute;left:1106px;top:555px;width:52px;height:52px;border-radius:6px;background:var(--orange);display:flex;align-items:center;justify-content:center}

/* feature strip */
.features{height:92px;background:var(--cream)}
.features .wrap{display:flex;height:92px;align-items:center;padding-left:18px}
.feature{display:flex;align-items:center;gap:10px;font-size:10px;font-weight:500;line-height:1.4;width:228px}

/* about */
.about{height:483px;background:var(--cream);position:relative}
.about-photo{position:absolute;left:149px;top:56px;width:438px;height:298px;border-radius:14px;background:linear-gradient(180deg,#e8872e 0%,#c9521e 55%,#3c1f22 100%)}
.about-frame{position:absolute;left:124px;top:163px;width:210px;height:210px;border:1.5px solid var(--orange);border-right:none;border-radius:18px 0 0 18px}
.about-text{position:absolute;left:650px;top:128px;width:355px}
.about-text h2{font-size:33px;line-height:1}
.about-text .accent-bar{margin:6px 0 14px}
.about-text p{font-size:10.3px;color:var(--muted);margin-bottom:10px}
.wave{position:absolute;left:0;width:1200px}

/* access */
.access{height:642px;position:relative;background:#fff}
.section-title{text-align:center;padding-top:70px}
.section-title h2{font-size:35px;line-height:1}
.grid3{display:grid;grid-template-columns:repeat(3,1fr);gap:9px}
.access .grid3{margin-top:34px;row-gap:12px}
.access-card{height:138px;border:1px solid var(--line);border-radius:6px;padding:34px 20px 0 30px;display:flex;gap:14px;box-shadow:0 2px 6px rgba(0,0,0,.03)}
.icon-sq{flex:none;width:40px;height:40px;background:var(--orange);border-radius:3px;display:flex;align-items:center;justify-content:center}
.access-card h3{font-size:14px;font-weight:600;line-height:1.2;color:var(--navy)}
.access-card p{font-size:9.5px;color:var(--muted);margin-top:6px;line-height:1.5}

/* modules */
.modules{height:530px;background:linear-gradient(180deg,#2c2752,#25214a);position:relative;color:#fff}
.modules .section-title h2{color:#fff}
.modules .section-title{padding-top:134px}
.mod-grid{display:grid;grid-template-columns:repeat(4,1fr);gap:7px;margin-top:24px}
.mod-card{height:179px;background:#fff;border-radius:5px;text-align:center;color:var(--navy);padding-top:22px}
.mod-card svg{margin:0 auto;display:block}
.mod-card h3{font-size:14px;font-weight:600;line-height:1.2;margin-top:12px}
.mod-card p{font-size:9.5px;color:var(--muted);margin-top:6px;line-height:1.5}

/* how */
.how{height:443px;background:var(--cream);position:relative}
.how-text{position:absolute;left:153px;top:137px;width:375px}
.how-text h2{font-size:33px;line-height:1}
.how-text .accent-bar{margin:6px 0 14px}
.how-text p{font-size:10px;color:var(--muted);line-height:1.65}
.how-photo{position:absolute;left:608px;top:47px;width:439px;height:299px;border-radius:14px;background:linear-gradient(180deg,#d9823c 0%,#7a4a5a 45%,#2b3658 100%)}
.how-frame{position:absolute;left:580px;top:222px;width:210px;height:190px;border:1.5px solid var(--orange);border-right:none;border-top:none;border-radius:0 0 0 18px}

/* unique */
.unique{height:469px;position:relative}
.unique .section-title{padding-top:90px}
.unique .grid3{margin-top:42px}
.uq-card{height:183px;border:1px solid var(--line);border-radius:6px;padding:72px 40px 0 40px;position:relative}
.uq-num{position:absolute;top:-29px;left:40px;width:62px;height:62px;background:var(--orange);color:#fff;font-weight:700;font-size:26px;display:flex;align-items:center;justify-content:center;border-radius:3px}
.uq-card h3{font-size:14px;font-weight:600;line-height:1.2;color:var(--navy)}
.uq-card p{font-size:9.5px;color:var(--muted);margin-top:10px;line-height:1.55}

/* news */
.news{height:590px;background:var(--cream);position:relative}
.news .section-title{padding-top:82px}
.view-all{position:absolute;right:0;top:100px;color:var(--orange);font-size:10.5px;text-decoration:underline}
.news .grid3{margin-top:30px}
.news-card{height:363px;background:#fff;border-radius:6px;overflow:hidden;border:1px solid var(--line)}
.news-img{height:196px}
.news-body{padding:26px 28px 0}
.news-body h3{font-size:14px;font-weight:600;line-height:1.2;color:var(--navy)}
.news-body p{font-size:9.5px;color:var(--muted);margin-top:8px;line-height:1.55}
.news-body time{display:block;color:var(--orange);font-size:9.5px;margin-top:4px}

/* cta */
.cta{height:148px;background:var(--navy);color:#fff}
.cta .wrap{display:flex;align-items:center;height:148px}
.cta h2{color:#fff;font-size:27px;line-height:1}
.cta p{font-size:10px;margin-top:4px;color:#ddd}
.cta-actions{margin-left:auto;display:flex;gap:6px}
.cta-actions .btn{height:28px;padding:0 28px;font-size:10px}

/* footer */
.footer{height:329px;background:#fff;position:relative}
.footer .wrap{display:flex;padding-top:80px}
.f-brand{width:240px;text-align:center}
.f-brand .brand-dot{display:block;width:40px;height:40px;margin:0 auto 10px}
.f-brand .brand-name{font-size:15px}
.socials{display:flex;gap:6px;justify-content:center;margin-top:14px}
.socials i{width:26px;height:26px;border-radius:50%;background:var(--navy);display:block}
.f-col{width:165px}
.f-col h4{font-size:13px;font-weight:600;color:var(--navy);margin-bottom:4px}
.f-col li{list-style:none;font-size:9.5px;line-height:2;color:var(--ink)}
.f-news{width:205px}
.f-news h4{font-size:13px;font-weight:600;color:var(--navy)}
.f-news p{font-size:9.5px;margin-top:4px;line-height:1.5}
.f-input{margin-top:12px;height:36px;border:1px solid var(--line);border-radius:3px;display:flex;align-items:center;justify-content:space-between;padding:0 12px;font-size:9.5px}
.to-top{position:absolute;left:1096px;top:54px;width:26px;height:26px;border-radius:50%;background:var(--orange)}
.f-bottom{position:absolute;left:150px;right:150px;bottom:0;height:36px;border-top:1px solid var(--line);display:flex;align-items:center;font-size:9.5px}
.pay{margin-left:auto;display:flex;gap:6px}
.pay i{width:30px;height:18px;border-radius:3px;background:#d9d6e4;display:block}
</style>
</head>
<body>

<header>
  <div class="topbar">
    <div class="wrap">
      <div class="brand">
        <span class="brand-dot"></span>
        <div class="brand-name">TAMBERLY CO</div>
      </div>
      <div class="search-top"><span>Search for projects, companies, tenders, news...</span>
        <svg width="10" height="10" viewBox="0 0 10 10"><circle cx="4" cy="4" r="3" fill="none" stroke="#29244f" stroke-width="1.4"/><path d="M6.3 6.3 9 9" stroke="#29244f" stroke-width="1.4"/></svg></div>
      <div class="top-actions">
        <span class="lang"><i></i>En ▾</span>
        <span class="btn-login"><svg width="9" height="10" viewBox="0 0 9 10"><circle cx="4.5" cy="3" r="2.2" fill="none" stroke="#29244f"/><path d="M.6 9.5c.6-2.4 2-3.4 3.9-3.4s3.3 1 3.9 3.4" fill="none" stroke="#29244f"/></svg>Login</span>
        <span class="btn-register">Register</span>
      </div>
    </div>
  </div>
  <nav class="mainnav">
    <ul>
      <li class="active">Home</li><li>Industry Insights</li><li>Oil &amp; Gas Opportunities</li><li>Supplier &amp; Company Network</li><li>Legal Framework</li><li>News</li><li>Contact Us</li>
    </ul>
  </nav>
</header>

<section class="hero">
  <div class="hero-photo" role="img" aria-label="Refinery at sunset with an engineer in a hard hat"></div>
  <div class="hero-inner">
    <h1>Access Mozambique’s Oil &amp; Gas Industry<br>Intelligence in One Platform</h1>
    <p>Tamberly is a modern online connection and consulting platform designed to facilitate access to the Mozambican Oil and Gas industry through premium industry insights, supplier information, tenders, legal frameworks, and strategic project data.</p>
    <div class="search-panel">
      <div class="sp-row">
        <div class="sp-field"><span>Search Keywords</span><div class="sp-input" style="width:165px">e.g. project, Company Tender...</div></div>
        <div class="sp-field"><span>Category</span><div class="sp-input" style="width:165px">All Categories <b>⌄</b></div></div>
        <div class="sp-field"><span>Location</span><div class="sp-input" style="width:165px">All Locations <b>⌄</b></div></div>
        <div class="sp-search"><svg width="9" height="9" viewBox="0 0 10 10"><circle cx="4" cy="4" r="3" fill="none" stroke="#fff" stroke-width="1.4"/><path d="M6.3 6.3 9 9" stroke="#fff" stroke-width="1.4"/></svg>Search</div>
      </div>
      <div class="sp-tabs"><span><i></i>Projects</span><span><i></i>Companies</span><span><i></i>Tenders</span><span><i></i>Suppliers</span><span><i></i>News</span></div>
    </div>
    <div class="hero-cta"><span class="btn btn-orange">Register Now</span><span class="btn btn-outline">Explore Opportunities</span></div>
  </div>
  <div class="chat-bubble">Hi! How can we help you today?</div>
  <div class="chat-btn"><svg width="26" height="22" viewBox="0 0 26 22"><path d="M3 2h20a2 2 0 0 1 2 2v11a2 2 0 0 1-2 2H10l-6 4v-4H3a2 2 0 0 1-2-2V4a2 2 0 0 1 2-2z" fill="#fff"/><circle cx="8" cy="9.5" r="1.5" fill="#ee4a1c"/><circle cx="13" cy="9.5" r="1.5" fill="#ee4a1c"/><circle cx="18" cy="9.5" r="1.5" fill="#ee4a1c"/></svg></div>
</section>

<section class="features">
  <div class="wrap">
    <div class="feature"><svg width="32" height="32" viewBox="0 0 32 32"><circle cx="16" cy="16" r="12" fill="none" stroke="#ee4a1c" stroke-width="2"/><path d="M16 9v7l5 3" stroke="#ee4a1c" stroke-width="2" fill="none"/></svg><span>Real-Time Data Sync<br>Automated &amp; Reliable</span></div>
    <div class="feature"><svg width="36" height="28" viewBox="0 0 36 28"><rect x="2" y="4" width="28" height="19" rx="2" fill="none" stroke="#ee4a1c" stroke-width="2"/><path d="M2 10h28" stroke="#ee4a1c" stroke-width="2"/><rect x="24" y="15" width="10" height="10" rx="1" fill="#ee4a1c"/></svg><span>Secure Payments<br>Safe &amp; Encrypted</span></div>
    <div class="feature"><svg width="34" height="32" viewBox="0 0 34 32"><circle cx="17" cy="16" r="4" fill="#ee4a1c"/><circle cx="5" cy="5" r="3" fill="none" stroke="#ee4a1c" stroke-width="2"/><circle cx="29" cy="5" r="3" fill="none" stroke="#ee4a1c" stroke-width="2"/><circle cx="5" cy="27" r="3" fill="none" stroke="#ee4a1c" stroke-width="2"/><circle cx="29" cy="27" r="3" fill="none" stroke="#ee4a1c" stroke-width="2"/><path d="M7 7l7 7M27 7l-7 7M7 25l7-7M27 25l-7-7" stroke="#ee4a1c" stroke-width="1.5"/></svg><span>Active Community<br>Network &amp; Connect</span></div>
    <div class="feature"><svg width="34" height="32" viewBox="0 0 34 32"><path d="M17 2l13 5v8c0 8-6 13-13 15C10 28 4 23 4 15V7z" fill="none" stroke="#ee4a1c" stroke-width="2"/><path d="M11 16l4 4 8-8" stroke="#ee4a1c" stroke-width="2" fill="none"/></svg><span>Trusted by Industry<br>Companies &amp; Professionals</span></div>
  </div>
</section>

<section class="about">
  <div class="about-frame"></div>
  <div class="about-photo" role="img" aria-label="Offshore platform and tanker at sunset"></div>
  <div class="about-text">
    <h2>What is Tamberly?</h2>
    <span class="accent-bar"></span>
    <p>Tamberly is a unique online platform built to connect businesses, investors, suppliers, and professionals with valuable information about the Mozambican Oil &amp; Gas sector.</p>
    <p>Through a secure digital paywall system, users gain access to organized, up-to-date, and carefully selected industry information that supports better decision-making, market understanding, and business opportunities within Mozambique’s growing hydrocarbons industry.</p>
  </div>
  <svg class="wave" style="bottom:0" height="80" viewBox="0 0 1200 80" preserveAspectRatio="none"><path d="M0 40 C300 80 700 0 1200 20 V80 H0Z" fill="#fff"/><path d="M0 30 C300 70 700 -10 1200 10" fill="none" stroke="#e8e2d9" stroke-width="2"/></svg>
</section>

<section class="access">
  <div class="wrap">
    <div class="section-title"><h2>What You Will Access</h2><span class="accent-bar"></span></div>
    <div class="grid3">
      <div class="access-card"><span class="icon-sq"><svg width="18" height="20" viewBox="0 0 18 20"><rect x="2" y="1" width="14" height="18" fill="none" stroke="#fff" stroke-width="1.6"/><path d="M5 6h8M5 10h8M5 14h5" stroke="#fff" stroke-width="1.6"/></svg></span><div><h3>Hydrocarbon Industry<br>Information</h3><p>General information and insights about Mozambique’s oil and gas sector.</p></div></div>
      <div class="access-card"><span class="icon-sq"><svg width="20" height="20" viewBox="0 0 20 20"><circle cx="10" cy="10" r="4" fill="none" stroke="#fff" stroke-width="1.6"/><path d="M10 1v4M10 15v4M1 10h4M15 10h4M3.6 3.6l2.8 2.8M13.6 13.6l2.8 2.8M3.6 16.4l2.8-2.8M13.6 6.4l2.8-2.8" stroke="#fff" stroke-width="1.6"/></svg></span><div><h3>Main Gas<br>Projects</h3><p>Details about major gas and energy projects operating in Mozambique.</p></div></div>
      <div class="access-card"><span class="icon-sq"><svg width="18" height="20" viewBox="0 0 18 20"><rect x="2" y="2" width="14" height="16" fill="none" stroke="#fff" stroke-width="1.6"/><path d="M2 7h14M2 12h14" stroke="#fff" stroke-width="1.6"/></svg></span><div><h3>Supplier &amp; Company<br>Database</h3><p>Mozambican companies capable of meeting Level 3 supply requirements.</p></div></div>
      <div class="access-card"><span class="icon-sq"><svg width="22" height="18" viewBox="0 0 22 18"><circle cx="11" cy="5" r="3" fill="none" stroke="#fff" stroke-width="1.6"/><circle cx="4" cy="8" r="2" fill="none" stroke="#fff" stroke-width="1.4"/><circle cx="18" cy="8" r="2" fill="none" stroke="#fff" stroke-width="1.4"/><path d="M5 17c1-4 3-6 6-6s5 2 6 6" fill="none" stroke="#fff" stroke-width="1.6"/></svg></span><div><h3>Industry<br>Contacts</h3><p>Key contacts from NOCs, Operators, EPCs, and Second-Tier Suppliers.</p></div></div>
      <div class="access-card"><span class="icon-sq"><svg width="18" height="20" viewBox="0 0 18 20"><path d="M3 1h9l4 4v14H3z" fill="none" stroke="#fff" stroke-width="1.6"/><path d="M6 9h7M6 13h7" stroke="#fff" stroke-width="1.6"/></svg></span><div><h3>Tender<br>Opportunities</h3><p>Short, medium, and long-term tenders within the industry.</p></div></div>
      <div class="access-card"><span class="icon-sq"><svg width="14" height="20" viewBox="0 0 14 20"><circle cx="7" cy="6" r="4.5" fill="none" stroke="#fff" stroke-width="1.6"/><path d="M7 10.5V19M7 15h3" stroke="#fff" stroke-width="1.6"/></svg></span><div><h3>Ownership &amp;<br>Access</h3><p>Information related to hydrocarbon reserves and sector participation.</p></div></div>
      <div class="access-card"><span class="icon-sq"><svg width="22" height="20" viewBox="0 0 22 20"><path d="M11 2v16M5 18h12M3 5h16M3 5l-2 6h4zM19 5l-2 6h4z" fill="none" stroke="#fff" stroke-width="1.5"/></svg></span><div><h3>Legal<br>Framework</h3><p>Mozambican local content regulations and legal structures.</p></div></div>
      <div class="access-card"><span class="icon-sq"><svg width="20" height="18" viewBox="0 0 20 18"><path d="M2 17V9M6 17V6M10 17V8M14 17V4M18 17V2" stroke="#fff" stroke-width="2"/></svg></span><div><h3>Local Company<br>Capacity</h3><p>Business integration opportunities within the oil and gas sector.</p></div></div>
      <div class="access-card"><span class="icon-sq"><svg width="20" height="16" viewBox="0 0 20 16"><path d="M2 8l6 6L18 2" fill="none" stroke="#fff" stroke-width="2.4"/></svg></span><div><h3>Tender Application<br>Guidance</h3><p>Support and information on applying for industry tenders.</p></div></div>
    </div>
  </div>
  <svg class="wave" style="bottom:0" height="70" viewBox="0 0 1200 70" preserveAspectRatio="none"><path d="M0 30 C250 70 600 10 900 40 S1150 30 1200 20 V70 H0Z" fill="#2c2752"/></svg>
</section>

<section class="modules" role="region" aria-label="Interactive modules">
  <div class="wrap">
    <div class="section-title"><h2>Interactive Modules</h2><span class="accent-bar"></span></div>
    <div class="mod-grid">
      <div class="mod-card"><svg width="52" height="44" viewBox="0 0 52 44"><rect x="6" y="4" width="40" height="30" rx="2" fill="none" stroke="#ee4a1c" stroke-width="2"/><path d="M14 28V20M22 28V14M30 28V18M38 28V10" stroke="#ee4a1c" stroke-width="3"/><path d="M16 40h20" stroke="#ee4a1c" stroke-width="2"/></svg><h3>Market Intelligence<br>Dashboard</h3><p>Real-time market data &amp;<br>visual analytics.</p></div>
      <div class="mod-card"><svg width="52" height="44" viewBox="0 0 52 44"><circle cx="24" cy="20" r="14" fill="none" stroke="#ee4a1c" stroke-width="2"/><path d="M24 6v14h14" fill="none" stroke="#ee4a1c" stroke-width="2"/><circle cx="38" cy="34" r="7" fill="none" stroke="#ee4a1c" stroke-width="2"/><path d="M38 30v8" stroke="#ee4a1c" stroke-width="2"/></svg><h3>Investment<br>Opportunities</h3><p>Discover lucrative opportunities<br>in Mozambique.</p></div>
      <div class="mod-card"><svg width="52" height="44" viewBox="0 0 52 44"><circle cx="26" cy="20" r="14" fill="none" stroke="#ee4a1c" stroke-width="2"/><circle cx="26" cy="16" r="4" fill="none" stroke="#ee4a1c" stroke-width="2"/><path d="M18 28c2-4 5-6 8-6s6 2 8 6" fill="none" stroke="#ee4a1c" stroke-width="2"/><path d="M14 40h24" stroke="#ee4a1c" stroke-width="2"/></svg><h3>Business<br>Matching</h3><p>Connect with the right partners<br>&amp; suppliers.</p></div>
      <div class="mod-card"><svg width="52" height="44" viewBox="0 0 52 44"><path d="M12 2h22l8 8v32H12z" fill="none" stroke="#ee4a1c" stroke-width="2"/><path d="M18 32l6-8 5 4 7-10" fill="none" stroke="#ee4a1c" stroke-width="2"/></svg><h3>Custom<br>Reports</h3><p>Generate and export tailored<br>industry reports.</p></div>
    </div>
  </div>
  <svg class="wave" style="bottom:0" height="70" viewBox="0 0 1200 70" preserveAspectRatio="none"><path d="M0 60 C300 10 700 50 1200 0 V70 H0Z" fill="#f4f1ec"/></svg>
</section>

<section class="how">
  <div class="how-text">
    <h2>How the Platform Works</h2>
    <span class="accent-bar"></span>
    <p>The platform operates through a secure automated payment system that grants registered users access to premium and exclusive content. By subscribing, users receive organized industry intelligence designed to save time, improve market access, and support strategic business growth within Mozambique’s energy sector.</p>
  </div>
  <div class="how-frame"></div>
  <div class="how-photo" role="img" aria-label="Offshore rig at dusk with a laptop showing secure data dashboards"></div>
</section>

<section class="unique">
  <div class="wrap">
    <div class="section-title"><h2>Why Tamberly is Unique</h2><span class="accent-bar"></span></div>
    <div class="grid3">
      <div class="uq-card"><span class="uq-num">01</span><h3>Up-to-Date Industry<br>Intelligence</h3><p>Receive frequent updates about developments in Mozambique’s Oil &amp; Gas sector.</p></div>
      <div class="uq-card"><span class="uq-num">02</span><h3>High-Quality Curated<br>Information</h3><p>Access carefully selected and synthesized information tailored to industry stakeholders.</p></div>
      <div class="uq-card"><span class="uq-num">03</span><h3>Time-Saving<br>Access</h3><p>Avoid spending hours searching through scattered online sources with organized and accessible content in one platform.</p></div>
    </div>
  </div>
</section>

<section class="news">
  <svg class="wave" style="top:0" height="60" viewBox="0 0 1200 60" preserveAspectRatio="none"><path d="M0 0 H1200 V30 C800 0 400 60 0 20Z" fill="#fff"/></svg>
  <div class="wrap">
    <div class="section-title"><h2>Latest Industry News</h2><span class="accent-bar"></span></div>
    <span class="view-all">View All</span>
    <div class="grid3">
      <article class="news-card"><div class="news-img" role="img" aria-label="Illuminated offshore platform at twilight" style="background:linear-gradient(180deg,#3c5a86,#d98a3c 70%,#2a2a3a)"></div><div class="news-body"><h3>Mozambique Opens New Offshore<br>Licensing Round</h3><p>The government of Mozambique has announced a new licensing round for offshore exploration blocks in the Rovuma Basin.</p><time>May 20, 2025</time></div></article>
      <article class="news-card"><div class="news-img" role="img" aria-label="LNG processing plant with pipes and tanks" style="background:linear-gradient(180deg,#8aa0b8,#5a6a7c 55%,#2f3d55)"></div><div class="news-body"><h3>Norvane Energies Advances<br>LNG Project</h3><p>Norvane Energies confirms progress on the LNG project in northern Mozambique, boosting energy development.</p><time>May 20, 2025</time></div></article>
      <article class="news-card"><div class="news-img" role="img" aria-label="Worker in orange coveralls turning a valve at a plant" style="background:linear-gradient(135deg,#4a7a5a,#c9b36a 50%,#d0642c)"></div><div class="news-body"><h3>Local Content<br>Regulations Update</h3><p>New local content regulations aim to increase Mozambican participation in the oil and gas industry.</p><time>May 20, 2025</time></div></article>
    </div>
  </div>
</section>

<section class="cta">
  <div class="wrap">
    <div><h2>Start Exploring Mozambique’s Oil &amp; Gas Opportunities</h2><p>Register today to access premium industry information, supplier networks, tenders, and strategic market insights through Tamberly.</p></div>
    <div class="cta-actions"><span class="btn btn-outline">See Pricing</span><span class="btn btn-orange">Register Now</span></div>
  </div>
</section>

<footer class="footer">
  <span class="to-top"></span>
  <div class="wrap">
    <div class="f-brand">
      <span class="brand-dot"></span>
      <div class="brand-name">TAMBERLY CO</div>
      <div class="socials"><i></i><i></i><i></i><i></i></div>
    </div>
    <div class="f-col"><h4>Quick Links</h4><ul><li>Home</li><li>Industry Insights</li><li>Oil &amp; Gas Opportunities</li><li>News</li><li>Phong</li></ul></div>
    <div class="f-col" style="width:153px"><h4>Resources</h4><ul><li>Legal Framework</li><li>Supplier Network</li><li>FAQS</li><li>Contact Us</li><li>Sitemap</li></ul></div>
    <div class="f-col" style="width:137px"><h4>Support</h4><ul><li>Help Center</li><li>Out Support</li><li>Terms of Use</li><li>Privacy Policy</li></ul></div>
    <div class="f-news"><h4>Subscribe to Our Newsletter</h4><p>Get the latest industry news and updates delivered to your inbox</p><div class="f-input"><span>Email Address</span><svg width="10" height="10" viewBox="0 0 10 10"><path d="M1 5 9 1 6 9 5 6z" fill="#ee4a1c"/></svg></div></div>
  </div>
  <div class="f-bottom"><span>© 2026 by Tamberly Co. All Rights Reserved.</span><div class="pay"><i></i><i></i><i></i><i></i><i></i></div></div>
</footer>

</body>
</html>
```